I-71 Website for Washington D.C Cannabis Business

We need a website with a 21+ age (yes/no/captcha) verification
5 Pages listed on a top banner
Home/Splash Page-Should send back to splash & ask for 21+ veri
Shop-
about Us
Blog
Contact us:

Content for pages:
Splash Page - Contains How it works with 1-6 steps
1. Register for Rewards Or Head to {Link} for more anonymous Use
2. Choose Cookies & Free Gifts
3. Submit Address & Order
4.Recieve Confirmation Text
5.Send Separate Selfie and Clear Drivers License Picture
6.Enjoy Your Cookies and Free Gifts

Shop/Menu Page - Empty with top banner (will fill in this section)

Home- Should link back to Splash page
About Us-
"Welcome to Marlow Treats, where everyday is a marlow day! We believe that everyone who chooses to enjoy the medicinal and relaxing benefits cannabis, should have safe and reliable access. And no matter your lifestyle or level of wellness, you deserve access to friendly customer service and professional courtesy. At Marlow Treats we provide Artisan Cookies that come with I-71 Gifted premium exotic cannabis + edibles & accessories. We provide an excellent variety of cookies and gifts, and all purchases improve your community!

For every 5 Cookies you purchase we donate 50 Sandwiches to Local DC Organizations that help our community members in need. In this way, you’ll be supporting the local DC community by purchasing from Marlow Treats (We also have Sandwich Rewards!!)

Marlow Treats is and always will be committed to providing DC The Best Service, Gifts & Experience. Always. We are committed to setting a standard for the gifting business in DC.

We appreciate you taking the time to check us out! We are here for all of your I-71 compliant needs.

Need to reach us? Please send all business related inquiries/compliments/complaints to marlowtreatsdc@brimvale.com and we will reach out ASAP. We look forward to hearing from you!

-MT

Blog- This should be Fillable
Contact US: Should be fillable with text or graphic

Similar Websites to check out: https://www.dcfernlotte.com/
https://www.amberloftwick.com/

Target Market(s)

DC/Cannabis market

Coding

Coded - Design and coding required

Number of Pages Required

5+ page

Font styles to use
Other font styles liked:
• Sans Serif

Colors
0455a3
33b8a4
ffffff

Requirements
Must have
• 21+ age (yes/no/captcha) verification
I-71 Compliant
Color match the green to the logo
Nice to have
• I would like the website to have a fresh and fun look....without being corny
Cookie buttons (menu etc that look like a cookie)
Should not have
• No pictures of Marihuana

```html
<!DOCTYPE html>
<html lang="en">
<head>
<meta charset="utf-8">
<title>Marlow Treats – How It Works</title>
<link href="https://fonts.googleapis.com/css2?family=Montserrat:wght@600;700;800&family=Nunito+Sans:wght@400;600&display=swap" rel="stylesheet">
<style>
  :root {
    --page-bg: #ffffff;
    --header-bg: #e9f6fc;
    --brand-blue: #2424e0;
    --brand-navy: #1a1ab8;
    --brand-green: #22e02a;
    --text-dark: #1d1d24;
    --text-light: #ffffff;
    --no-button: #7c7cef;
    --hero-dark: #3b2c22;
    --hero-mid: #7a6048;
    --hero-light: #a88a66;
    --dim: rgba(12, 12, 16, 0.72);
  }
  * { box-sizing: border-box; margin: 0; padding: 0; }
  html, body { width: 950px; height: 1200px; overflow: hidden; background: var(--page-bg); }
  body { position: relative; font-family: "Nunito Sans", Arial, sans-serif; color: var(--text-dark); }

  .screen {
    position: absolute; left: 50px; width: 848px; height: 497px;
    box-shadow: 0 8px 30px rgba(0,0,0,0.18); overflow: hidden;
  }
  .screen--home { top: 57px; }
  .screen--age-gate { top: 644px; }

  .site-header {
    height: 82px; background: var(--header-bg);
    display: flex; flex-direction: column; align-items: center; justify-content: center; gap: 6px;
  }
  .brand-mark { width: 34px; height: 34px; border-radius: 50%; background: var(--brand-green); }
  .brand-name {
    font-family: "Montserrat", Arial, sans-serif; font-weight: 800; font-size: 11px;
    letter-spacing: 0.5px; color: var(--brand-navy);
  }

  .main-nav { height: 29px; background: var(--brand-blue); position: relative; }
  .main-nav a {
    position: absolute; top: 0; line-height: 29px; transform: translateX(-50%);
    font-family: "Nunito Sans", Arial, sans-serif; font-weight: 600; font-size: 9.5px;
    color: var(--text-light); text-decoration: none; white-space: nowrap;
  }

  .hero { position: relative; height: 344px; }
  .hero-photo {
    position: absolute; inset: 0;
    background: radial-gradient(ellipse at 70% 35%, var(--hero-light) 0%, var(--hero-mid) 35%, var(--hero-dark) 80%);
  }
  .hero-shade { position: absolute; inset: 0; background: rgba(0,0,0,0.35); }
  .hero-title {
    position: absolute; top: 78px; left: 0; right: 0; text-align: center;
    font-family: "Montserrat", Arial, sans-serif; font-weight: 700; font-size: 22px; color: var(--text-light);
  }
  .step { position: absolute; top: 136px; width: 140px; transform: translateX(-50%); text-align: center; color: var(--text-light); }
  .step-icon { display: block; width: 36px; height: 36px; margin: 0 auto; }
  .step-label {
    margin-top: 10px; font-family: "Montserrat", Arial, sans-serif; font-weight: 800;
    font-size: 14.5px; letter-spacing: 1px;
  }
  .step-text { margin-top: 7px; font-size: 9.5px; line-height: 16px; }
  .shop-button {
    position: absolute; left: 347px; top: 286px; width: 154px; height: 30px;
    background: var(--brand-blue); color: var(--text-light); text-decoration: none;
    display: flex; align-items: center; justify-content: center; gap: 7px;
    font-family: "Montserrat", Arial, sans-serif; font-weight: 700; font-size: 10px; letter-spacing: 0.8px;
  }

  .site-footer { height: 42px; background: var(--header-bg); position: relative; font-size: 10.5px; }
  .copyright { position: absolute; left: 80px; top: 0; line-height: 42px; }
  .footer-links a {
    position: absolute; top: 0; line-height: 42px; transform: translateX(-50%);
    font-size: 9px; color: var(--text-dark); text-decoration: none;
  }
  .footer-divider { position: absolute; left: 686px; top: 10px; width: 1px; height: 22px; background: var(--brand-blue); }

  .dim-layer { position: absolute; inset: 0; background: var(--dim); }

  .age-modal {
    position: absolute; left: 227px; top: 137px; width: 394px; height: 223px;
    background: var(--brand-blue); color: var(--text-light); text-align: center;
  }
  .age-modal .close { position: absolute; left: 373px; top: 10px; font-size: 12px; }
  .age-modal .brand-mark { width: 40px; height: 40px; margin: 30px auto 0; }
  .age-modal .brand-name { color: var(--text-light); font-size: 11.5px; margin-top: 10px; }
  .age-modal .prompt { margin-top: 30px; font-size: 11.5px; }
  .age-actions { position: absolute; top: 169px; left: 70px; display: flex; gap: 16px; }
  .age-actions span {
    width: 119px; height: 30px; line-height: 30px;
    font-family: "Montserrat", Arial, sans-serif; font-weight: 700; font-size: 9.5px; letter-spacing: 0.8px;
  }
  .btn-yes { background: var(--text-light); color: var(--brand-blue); }
  .btn-no { background: var(--no-button); color: var(--text-light); }
</style>
</head>
<body>

<section class="screen screen--home">
  <header class="site-header">
    <span class="brand-mark"></span>
    <span class="brand-name">MARLOW TREATS</span>
  </header>
  <nav class="main-nav">
    <a style="left:183px">HOME</a><a style="left:258px">SHOP</a><a style="left:331px">BLOG</a>
    <a style="left:408px">ABOUT</a><a style="left:490px">EVENTS</a><a style="left:581px">NEW PAGE</a><a style="left:665px">MORE</a>
  </nav>
  <div class="hero">
    <div class="hero-photo" role="img" aria-label="Close-up photo of oatmeal cookies on a wooden table"></div>
    <div class="hero-shade"></div>
    <h1 class="hero-title">HOW TO WORKS</h1>

    <div class="step" style="left:122px">
      <svg class="step-icon" viewBox="0 0 36 36" fill="none" stroke="var(--brand-green)" stroke-width="1.6"><circle cx="18" cy="14" r="11"/><circle cx="18" cy="14" r="7"/><path d="M11 23l-4 9 5-2 2 4 3-8M25 23l4 9-5-2-2 4-3-8"/></svg>
      <div class="step-label">STEP 1</div>
      <p class="step-text">Register for Rewards</p>
    </div>
    <div class="step" style="left:237px">
      <svg class="step-icon" viewBox="0 0 36 36" fill="none" stroke="var(--brand-green)" stroke-width="1.6"><circle cx="17" cy="19" r="13"/><circle cx="12" cy="16" r="1.4"/><circle cx="19" cy="13" r="1.4"/><circle cx="15" cy="23" r="1.4"/><circle cx="22" cy="21" r="1.4"/></svg>
      <div class="step-label">STEP 2</div>
      <p class="step-text">Choose Cookies &amp;<br>Free Gifts</p>
    </div>
    <div class="step" style="left:349px">
      <svg class="step-icon" viewBox="0 0 36 36" fill="none" stroke="var(--brand-green)" stroke-width="1.6"><path d="M18 26s-8-8-8-14a8 8 0 0116 0c0 6-8 14-8 14z"/><circle cx="18" cy="12" r="3.5"/><path d="M8 26l-5 8h30l-5-8"/></svg>
      <div class="step-label">STEP 3</div>
      <p class="step-text">Submit Address &amp;<br>Order</p>
    </div>
    <div class="step" style="left:461px">
      <svg class="step-icon" viewBox="0 0 36 36" fill="none" stroke="var(--brand-green)" stroke-width="1.8"><circle cx="18" cy="18" r="15"/><path d="M11 18l5 5 9-10"/></svg>
      <div class="step-label">STEP 4</div>
      <p class="step-text">Recieve Confirmation<br>Text</p>
    </div>
    <div class="step" style="left:597px">
      <svg class="step-icon" viewBox="0 0 36 36" fill="none" stroke="var(--brand-green)" stroke-width="1.6"><rect x="11" y="4" width="14" height="28" rx="2"/><path d="M16 28h4"/></svg>
      <div class="step-label">STEP 5</div>
      <p class="step-text">Send Separate Selfie &amp;<br>Clear Drivers License Picture</p>
    </div>
    <div class="step" style="left:730px">
      <svg class="step-icon" viewBox="0 0 36 36" fill="none" stroke="var(--brand-green)" stroke-width="1.6"><rect x="8" y="16" width="20" height="16"/><path d="M6 12h24v4H6zM18 12v20"/></svg>
      <div class="step-label">STEP 6</div>
      <p class="step-text">Enjoy Your Cookies<br>&amp; Free Gifts</p>
    </div>

    <a class="shop-button">CONTINUE TO SHOP
      <svg width="10" height="10" viewBox="0 0 10 10"><circle cx="5" cy="5" r="5" fill="#fff"/><path d="M4 2.8L6.2 5 4 7.2" stroke="var(--brand-blue)" stroke-width="1.4" fill="none"/></svg>
    </a>
  </div>
  <footer class="site-footer">
    <span class="copyright">Copyright © 2021 | All rights reserved</span>
    <span class="footer-links"><a style="left:641px">Privacy Policy</a><a style="left:737px">Terms and Use</a></span>
    <span class="footer-divider"></span>
  </footer>
</section>

<section class="screen screen--age-gate">
  <header class="site-header">
    <span class="brand-mark"></span>
    <span class="brand-name">MARLOW TREATS</span>
  </header>
  <nav class="main-nav">
    <a style="left:183px">HOME</a><a style="left:258px">SHOP</a><a style="left:331px">BLOG</a>
    <a style="left:408px">ABOUT</a><a style="left:490px">EVENTS</a><a style="left:581px">NEW PAGE</a><a style="left:665px">MORE</a>
  </nav>
  <div class="hero">
    <div class="hero-photo" role="img" aria-label="Close-up photo of oatmeal cookies on a wooden table"></div>
    <div class="hero-shade"></div>
    <h1 class="hero-title">HOW TO WORKS</h1>
    <div class="step" style="left:122px">
      <svg class="step-icon" viewBox="0 0 36 36" fill="none" stroke="var(--brand-green)" stroke-width="1.6"><circle cx="18" cy="14" r="11"/><circle cx="18" cy="14" r="7"/><path d="M11 23l-4 9 5-2 2 4 3-8M25 23l4 9-5-2-2 4-3-8"/></svg>
      <div class="step-label">STEP 1</div>
      <p class="step-text">Register for Rewards</p>
    </div>
    <div class="step" style="left:237px">
      <svg class="step-icon" viewBox="0 0 36 36" fill="none" stroke="var(--brand-green)" stroke-width="1.6"><circle cx="17" cy="19" r="13"/></svg>
      <div class="step-label">STEP 2</div>
      <p class="step-text">Choose Cookies &amp;<br>Free Gifts</p>
    </div>
    <div class="step" style="left:597px">
      <div class="step-label" style="margin-top:46px">STEP 5</div>
      <p class="step-text">Send Separate Selfie &amp;<br>Clear Drivers License Picture</p>
    </div>
    <div class="step" style="left:730px">
      <svg class="step-icon" viewBox="0 0 36 36" fill="none" stroke="var(--brand-green)" stroke-width="1.6"><rect x="8" y="16" width="20" height="16"/><path d="M6 12h24v4H6zM18 12v20"/></svg>
      <div class="step-label">STEP 6</div>
      <p class="step-text">Enjoy Your Cookies<br>&amp; Free Gifts</p>
    </div>
    <a class="shop-button">CONTINUE TO SHOP
      <svg width="10" height="10" viewBox="0 0 10 10"><circle cx="5" cy="5" r="5" fill="#fff"/><path d="M4 2.8L6.2 5 4 7.2" stroke="var(--brand-blue)" stroke-width="1.4" fill="none"/></svg>
    </a>
  </div>
  <footer class="site-footer">
    <span class="copyright">Copyright © 2021 | All rights reserved</span>
    <span class="footer-links"><a style="left:641px">Privacy Policy</a><a style="left:737px">Terms and Use</a></span>
    <span class="footer-divider"></span>
  </footer>

  <div class="dim-layer"></div>

  <div class="age-modal" role="dialog" aria-label="Age verification">
    <span class="close">X</span>
    <div class="brand-mark"></div>
    <div class="brand-name">MARLOW TREATS</div>
    <p class="prompt">Please verify your age before shopping our Products!</p>
    <div class="age-actions">
      <span class="btn-yes">Yes, I am over 21.</span>
      <span class="btn-no">No</span>
    </div>
  </div>
</section>

</body>
</html>
```